A card that says it all!

Hey there!
We are in need of a business card design for a facility service provider company named Kelbrook Works.
I would like a business card design that is not focus on a person but more on the company. A place for a QR code would be nice, and i will have that code direct to our request form online. "Scanner to schedule service" or "Scan to schedule a estimate". Something like that. Kelbrook Works is the Industry Leader in Facility Remodeling, Rollouts, and Capital Repairs

Target Market(s)

large facilities needing services such as remodels. HVAC, plumbing, electrical

Industry/Entity Type

Industry Leader in Facility Remodeling, Rollouts, and Capital Repairs

Contact Information for Business Card

phone number: 418.527.3096; email: info@kelbrookworks.us; Website: www.KelbrookWorks.us

Requirements
Must have
• sleak; classic
Should not have
• No houses or tools art

```html
<!DOCTYPE html>
<html lang="en">
<head>
<meta charset="utf-8">
<title>Kelbrook Works — Business Card</title>
<link href="https://fonts.googleapis.com/css2?family=Tinos:wght@400;700&display=swap" rel="stylesheet">
<style>
  :root {
    --backdrop: #d3d2d2;
    --brand-blue: #3461b6;
    --card-white: #f4f4f4;
    --ink: #3a3a3a;
    --title-blue: #5a86d8;
    --on-blue: #ffffff;
    --qr-fill: #dcdcdc;
  }
  * { margin: 0; padding: 0; box-sizing: border-box; }
  html, body {
    width: 1200px; height: 1000px; overflow: hidden;
    background: var(--backdrop);
    font-family: "Tinos", "Times New Roman", serif;
  }
  .stage {
    position: relative; width: 1200px; height: 1000px;
    display: flex; align-items: center; justify-content: center; gap: 60px;
  }
  .card {
    position: relative; width: 480px; height: 274px;
    box-shadow: 0 6px 18px rgba(0,0,0,0.12);
    overflow: hidden;
  }

  /* Front */
  .card-front {
    background: var(--brand-blue);
    display: flex; align-items: center; justify-content: center;
  }
  .company-name {
    color: var(--on-blue); font-size: 40px; font-weight: 400; letter-spacing: 1px;
  }

  /* Back */
  .card-back { background: var(--card-white); color: var(--ink); }
  .accent-bar { position: absolute; left: 0; height: 20px; background: var(--brand-blue); }
  .accent-bar.one   { top: 112px; width: 128px; }
  .accent-bar.two   { top: 144px; width: 122px; }
  .accent-bar.three { top: 176px; width: 112px; }

  .holder {
    position: absolute; left: 150px; width: 220px; top: 96px; text-align: center;
  }
  .holder-name { font-size: 21px; letter-spacing: 0.5px; }
  .holder-title {
    font-size: 11px; color: var(--title-blue); letter-spacing: 1px; margin-top: 3px;
  }

  .band {
    position: absolute; height: 30px;
    background: var(--brand-blue); color: var(--on-blue);
    display: flex; align-items: center; gap: 7px; font-size: 15px;
  }
  .band svg { width: 14px; height: 14px; flex: none; }
  .band-email { top: 150px; left: 290px; right: 0; padding-left: 14px; }
  .band-phone { top: 206px; left: 134px; width: 160px; padding-left: 14px; }

  .website {
    position: absolute; left: 306px; top: 212px; font-size: 14px; letter-spacing: 0.3px;
  }

  .qr-area {
    position: absolute; top: 22px; right: 22px; width: 92px; text-align: center;
  }
  .qr-slot {
    width: 70px; height: 70px; margin: 0 auto;
    background: var(--qr-fill); border: 2px solid var(--brand-blue);
  }
  .qr-caption {
    font-size: 9px; letter-spacing: 0.5px; color: var(--brand-blue); margin-top: 5px;
  }
</style>
</head>
<body>
<main class="stage">
  <section class="card card-front" aria-label="Card front">
    <span class="company-name">Kelbrook Works</span>
  </section>

  <section class="card card-back" aria-label="Card back">
    <div class="accent-bar one"></div>
    <div class="accent-bar two"></div>
    <div class="accent-bar three"></div>

    <div class="qr-area">
      <div class="qr-slot" role="img" aria-label="QR code linking to the online service request form"></div>
      <div class="qr-caption">SCAN TO SCHEDULE</div>
    </div>

    <div class="holder">
      <div class="holder-name">Evan Marlowe</div>
      <div class="holder-title">TITLE</div>
    </div>

    <div class="band band-email">
      <svg viewBox="0 0 24 24" fill="none" stroke="currentColor" stroke-width="2.2"><rect x="3" y="5" width="18" height="14"/><path d="M3 6l9 7 9-7"/></svg>
      info@kelbrookworks.us
    </div>

    <div class="band band-phone">
      <svg viewBox="0 0 24 24" fill="none" stroke="currentColor" stroke-width="2.4" stroke-linecap="round"><path d="M4 9c0-3 3-5 8-5s8 2 8 5l-3 2-2-3h-6l-2 3z"/><path d="M7 13v5h10v-5"/></svg>
      418 527 3096
    </div>

    <div class="website">www.KelbrookWorks.us</div>
  </section>
</main>
</body>
</html>
```